Consulting company needs website design

We need a simple, static website design for our consulting company. We are looking for a general design of the look and feel of the website. Initially, it will have these pages:
- Home
- About us
- Services
- Contact us
We have our own logo which I have attached to the brief.

We are looking for a simple website, with white background and the use of gray (darker) as the main theme. Simple fonts. The website should be responsive so it an be easily red in mobile devices.

As part of the project, we will need to receive at least the following items:
- Individual files with sample text to support the pages outlined above
- Necessary CSS files

Our current website is here: http://www.lantrovale.co/

Here are some examples of other website we like to be used as guideline:
- http://www.morvicaplanos.com/
-

Target Market(s)

Individuals and companies looking to hire our company to provide consulting services.

Industry/Entity Type

It Company

Coding

Coded - Design and coding required

Number of Pages Required

4 page

Font styles to use
Sans Serif

Requirements
Must have
• Main page should have the ability to embed Chirplet feed into it.
• We prefer the design to use gray tones.

```html
<!DOCTYPE html>
<html lang="en">
<head>
<meta charset="utf-8">
<title>Lantrovale Group SAS</title>
<link href="https://fonts.googleapis.com/css2?family=Raleway:wght@300;400;500&family=Open+Sans:wght@400;600&display=swap" rel="stylesheet">
<style>
:root{
  --navy:#2f3545;
  --navy-deep:#272c39;
  --text:#555a62;
  --muted:#6b6f76;
  --hex:#b5b5b5;
  --band:#f7f7f7;
  --white:#ffffff;
}
*{box-sizing:border-box;margin:0;padding:0}
html,body{width:965px;height:1200px;overflow:hidden;background:var(--white)}
body{position:relative;font-family:"Open Sans",Arial,sans-serif;color:var(--text)}
.site-header{position:absolute;left:0;top:0;width:965px;height:82px;border-top:2px solid #5d636c;background:var(--white)}
.brand{position:absolute;left:80px;top:11px;display:flex;align-items:center;gap:10px}
.brand-mark{width:60px;height:60px;border-radius:50%;border:1px solid #c9c9c9;background:#f1f1f1}
.brand-name{font-family:"Raleway",Arial,sans-serif;font-size:16px;line-height:19px;color:#5a5e66}
.main-nav{position:absolute;top:29px;left:450px;display:flex;align-items:center;font-family:"Raleway",Arial,sans-serif;font-size:11px;color:#666}
.main-nav a{text-decoration:none;color:inherit}
.nav-home{background:var(--navy);color:var(--white)!important;padding:6px 13px;border-radius:2px}
.nav-about{margin-left:49px}
.nav-services{margin-left:51px}
.nav-contact{margin-left:60px}
.nav-feed{position:absolute;left:846px;top:36px;font-family:"Raleway",Arial,sans-serif;font-size:11px;color:var(--navy);display:flex;align-items:center;gap:5px}
.nav-feed span.dot{width:9px;height:9px;border-radius:50%;background:var(--navy)}
.hero{position:absolute;left:0;top:82px;width:965px;height:414px;background:linear-gradient(180deg,#b7bcc4 0%,#8f96a3 45%,#4f5666 100%)}
.hero-quote{position:absolute;left:0;top:152px;width:965px;text-align:center;font-family:"Raleway",Arial,sans-serif;font-weight:300;font-size:30px;line-height:44px;color:var(--white);text-shadow:0 1px 3px rgba(0,0,0,.4)}
.hero-dots{position:absolute;top:259px;left:463px;display:flex;gap:6px}
.hero-dots i{width:9px;height:9px;border-radius:50%;border:1.5px solid var(--white)}
.hero-dots i.on{background:var(--white)}
.welcome{position:absolute;left:0;top:496px;width:965px;height:266px;text-align:center}
.section-title{font-family:"Raleway",Arial,sans-serif;font-weight:400;font-size:20px;color:var(--navy)}
.welcome .section-title{margin-top:28px}
.divider{margin:10px auto 0;width:164px;height:18px}
.welcome p{width:810px;margin:7px auto 0;font-size:10.6px;line-height:20.7px;color:var(--muted)}
.btn{display:inline-flex;align-items:center;gap:6px;background:var(--navy);color:var(--white);font-family:"Open Sans",Arial,sans-serif;font-weight:600;font-size:9.5px;padding:0 22px;height:30px;border-radius:2px;box-shadow:0 2px 3px rgba(0,0,0,.3);text-decoration:none}
.btn .arr{width:8px;height:8px;border-radius:50%;background:var(--white)}
.welcome .btn{margin-top:16px}
.services{position:absolute;left:0;top:762px;width:965px;height:310px;background:var(--band);text-align:center}
.services .section-title{margin-top:22px}
.service{position:absolute;top:68px;width:260px;text-align:center}
.service h3{font-family:"Raleway",Arial,sans-serif;font-weight:400;font-size:14.5px;color:#555;margin-top:8px}
.service p{font-size:11px;line-height:18.5px;color:var(--muted);margin-top:9px}
.service .btn{margin-top:12px;padding:0 19px}
.s1{left:70px}.s2{left:352px}.s3{left:635px}
.slider-arrow{position:absolute;top:148px;width:18px;height:24px}
.footer{position:absolute;left:0;top:1072px;width:965px;height:96px;background:var(--navy)}
.footer .brand{top:18px}
.footer .brand-mark{border-color:#e0e0e0;background:#e9e9e9}
.footer .brand-name{color:var(--white)}
.connect{position:absolute;right:80px;top:30px;text-align:right;font-family:"Raleway",Arial,sans-serif;color:var(--white)}
.connect h4{font-weight:400;font-size:15.5px}
.social{margin-top:8px;display:flex;gap:10px;justify-content:flex-end;font-family:"Open Sans",Arial,sans-serif;font-size:10px}
.legal{position:absolute;left:0;top:1168px;width:965px;height:32px;background:var(--navy-deep);color:var(--white);font-size:10px;line-height:32px}
.legal .copy{position:absolute;left:79px}
.legal .links{position:absolute;right:80px;display:flex;gap:14px}
</style>
</head>
<body>
<header class="site-header">
  <div class="brand"><span class="brand-mark"></span><span class="brand-name">Lantrovale<br>Group SAS</span></div>
  <nav class="main-nav">
    <a class="nav-home" href="#">Home</a>
    <a class="nav-about" href="#">About us</a>
    <a class="nav-services" href="#">Services</a>
    <a class="nav-contact" href="#">Contact us</a>
  </nav>
  <a class="nav-feed"><span class="dot"></span>Chirplet</a>
</header>

<section class="hero" role="img" aria-label="Photo of smiling business colleagues in a meeting">
  <p class="hero-quote">" Adoption implies change, and change<br>rarely happens overnight "</p>
  <div class="hero-dots"><i class="on"></i><i></i><i></i></div>
</section>

<section class="welcome">
  <h2 class="section-title">Welcome to Lantrovale Group SAS</h2>
  <svg class="divider" viewBox="0 0 164 18"><line x1="0" y1="9" x2="67" y2="9" stroke="#2f3545" stroke-width="1.2"/><line x1="97" y1="9" x2="164" y2="9" stroke="#2f3545" stroke-width="1.2"/><circle cx="82" cy="9" r="8" fill="#2f3545"/><circle cx="82" cy="9" r="3" fill="#fff"/></svg>
  <p>Lorem Ipsum is simply dummy text of the printing and typesetting industry. Lorem Ipsum has been the industry's standard dummy text ever since the 1500s, when an unknown printer took a galley of type and scrambled it to make a type specimen book. It has survived not only five centuries, but also the leap into electronic typesetting, remaining essentially unchanged. It was popularised in the 1960s with the release of Typeleaf sheets containing Lorem Ipsum passages, and more recently with desktop publishing software like Pressmark Layout including versions of Lorem Ipsum.Lorem Ipsum is simply dummy text of the printing and typesetting industry. Lorem Ipsum has been the industry's standard dummy text ever since the 1500s.</p>
  <a class="btn" href="#">READ MORE <span class="arr"></span></a>
</section>

<section class="services">
  <h2 class="section-title">Our Services</h2>
  <svg class="slider-arrow" style="left:33px" viewBox="0 0 18 24"><polyline points="13,3 5,12 13,21" fill="none" stroke="#111" stroke-width="4"/></svg>
  <svg class="slider-arrow" style="left:914px" viewBox="0 0 18 24"><polyline points="5,3 13,12 5,21" fill="none" stroke="#111" stroke-width="4"/></svg>

  <div class="service s1">
    <svg width="88" height="78" viewBox="0 0 88 78"><polygon points="22,0 66,0 88,39 66,78 22,78 0,39" fill="#b5b5b5"/><path d="M33 30l6 6M39 30l-6 6M50 46l6 6M56 46l-6 6M42 34q10-6 16 2" stroke="#fff" stroke-width="2" fill="none"/><circle cx="62" cy="35" r="3" fill="#fff"/><circle cx="38" cy="48" r="3" fill="#fff"/></svg>
    <h3>Strategy</h3>
    <p>Lorem Ipsum is simply dummy text of the printing and typesetting industry. Lorem Ipsum has been the industry's standard dummy.</p>
    <a class="btn" href="#">READ MORE <span class="arr"></span></a>
  </div>
  <div class="service s2">
    <svg width="88" height="78" viewBox="0 0 88 78"><polygon points="22,0 66,0 88,39 66,78 22,78 0,39" fill="#b5b5b5"/><rect x="25" y="46" width="7" height="10" fill="#fff"/><rect x="36" y="40" width="7" height="16" fill="#fff"/><rect x="47" y="34" width="7" height="22" fill="#fff"/><rect x="58" y="28" width="7" height="28" fill="#fff"/><polyline points="25,38 40,30 50,24 62,18" stroke="#fff" stroke-width="2" fill="none"/></svg>
    <h3>Strategy</h3>
    <p>Lorem Ipsum is simply dummy text of the printing and typesetting industry. Lorem Ipsum has been the industry's standard dummy.</p>
    <a class="btn" href="#">READ MORE <span class="arr"></span></a>
  </div>
  <div class="service s3">
    <svg width="88" height="78" viewBox="0 0 88 78"><polygon points="22,0 66,0 88,39 66,78 22,78 0,39" fill="#b5b5b5"/><rect x="40" y="22" width="28" height="20" fill="none" stroke="#fff" stroke-width="2"/><rect x="46" y="32" width="3" height="7" fill="#fff"/><rect x="52" y="29" width="3" height="10" fill="#fff"/><rect x="58" y="34" width="3" height="5" fill="#fff"/><rect x="28" y="34" width="7" height="24" fill="#fff"/><circle cx="31" cy="28" r="3.5" fill="#fff"/></svg>
    <h3>Strategy</h3>
    <p>Lorem Ipsum is simply dummy text of the printing and typesetting industry. Lorem Ipsum has been the industry's standard dummy.</p>
    <a class="btn" href="#">READ MORE <span class="arr"></span></a>
  </div>
</section>

<footer class="footer">
  <div class="brand"><span class="brand-mark"></span><span class="brand-name">Lantrovale<br>Group SAS</span></div>
  <div class="connect">
    <h4>Connect with us</h4>
    <div class="social"><span>Friendloop</span><span>Chirplet</span><span>Plusring</span></div>
  </div>
</footer>
<div class="legal">
  <span class="copy">2016 © Lantrovale group SAS.All Rights received.</span>
  <span class="links"><span>Recent Site Activity</span><span>Report Abuse</span><span>Print Page</span></span>
</div>
</body>
</html>
```